Business Card Design

I am a GP with interest in Dermatology and Aesthetic Medicin, performing Botulinum Toxin Type A and Dermal Fillers treatmets in Cosmetic Dermatology clinic.

I am looking for a white colour, good quality white paper card may be of some special texture with black calligraphic writing but easy to read and not to wiggly- professional- looking.

Really appreciate your help.

Halyna

Cosmetic Dermatology Clinic

Dr Halyna Korbutiak, MBBS, MRCGP, DPD

Tel: 07841 615 092
halyna@medmailbox.org.uk

```html
<!DOCTYPE html>
<html lang="en">
<head>
<meta charset="utf-8">
<title>Cosmetic Dermatology Clinic – Business Card</title>
<link rel="stylesheet" href="https://fonts.googleapis.com/css2?family=Open+Sans:wght@400;600&family=Yesteryear&display=swap">
<style>
  :root {
    --backdrop: #d4d4d6;
    --card: #ffffff;
    --teal: #2fb0bd;
    --ink: #1c1c1c;
    --text: #3a3a3a;
  }
  * { margin: 0; padding: 0; box-sizing: border-box; }
  html, body {
    width: 883px;
    height: 1200px;
    overflow: hidden;
    background: var(--backdrop);
  }
  .card {
    position: absolute;
    left: 161px;
    width: 560px;
    height: 313px;
    background: var(--card);
    box-shadow: 0 4px 10px rgba(0, 0, 0, 0.18);
  }
  .card--front { top: 272px; }
  .card--back { top: 615px; }

  .clinic-name {
    position: absolute;
    font-family: "Open Sans", sans-serif;
    font-weight: 600;
    font-size: 20px;
    color: var(--teal);
    white-space: nowrap;
    line-height: 1;
  }
  .clinic-dot {
    position: absolute;
    width: 9px;
    height: 9px;
    border-radius: 50%;
    background: var(--teal);
  }
  .card--front .clinic-dot { left: 400px; top: 196px; }
  .card--front .clinic-name { right: 26px; top: 224px; }
  .card--back .clinic-dot { left: 166px; top: 40px; }
  .card--back .clinic-name { left: 35px; top: 68px; }

  .doctor {
    position: absolute;
    right: 26px;
    top: 178px;
    text-align: right;
  }
  .doctor__name {
    font-family: "Yesteryear", cursive;
    font-size: 25px;
    color: var(--ink);
    line-height: 1.1;
  }
  .doctor__credentials {
    font-family: "Open Sans", sans-serif;
    font-size: 14px;
    color: var(--text);
    letter-spacing: 0.2px;
  }
  .divider {
    position: absolute;
    left: 35px;
    top: 221px;
    width: 355px;
    height: 1.5px;
    background: var(--teal);
  }
  .contacts {
    position: absolute;
    left: 35px;
    top: 242px;
    list-style: none;
    font-family: "Open Sans", sans-serif;
    font-size: 14.5px;
    color: var(--text);
    line-height: 22px;
  }
  .contacts li { display: flex; align-items: center; gap: 8px; }
  .contacts svg { width: 11px; height: 11px; fill: var(--teal); flex: none; }
</style>
</head>
<body>
  <section class="card card--front" aria-label="Card front">
    <span class="clinic-dot"></span>
    <p class="clinic-name">Cosmetic Dermatology Clinic</p>
  </section>

  <section class="card card--back" aria-label="Card back">
    <span class="clinic-dot"></span>
    <p class="clinic-name">Cosmetic Dermatology Clinic</p>

    <div class="doctor">
      <p class="doctor__name">Dr Halyna Korbutiak</p>
      <p class="doctor__credentials">MBBS, MRCGP, DPD</p>
    </div>
    <div class="divider"></div>

    <ul class="contacts">
      <li>
        <svg viewBox="0 0 12 12" aria-hidden="true"><path d="M1 3.5C1 2.5 3 1.5 6 1.5S11 2.5 11 3.5V5H8.5V4H3.5V5H1Z M2.5 6.2 4 5h4l1.5 1.2V10.5h-7Z M6 6.8a1.3 1.3 0 1 0 0.01 0Z"/></svg>
        07841 615 092
      </li>
      <li>
        <svg viewBox="0 0 12 12" aria-hidden="true"><path d="M1 2.5h10v1L6 6.8 1 3.5Z M1 4.8l5 3.3 5-3.3V9.5H1Z"/></svg>
        halyna@medmailbox.org.uk
      </li>
    </ul>
  </section>
</body>
</html>
```